Alternative Health business needs a self help book cover design

Silver Brook Wellness requires an E book and print cover design for a new self help book titled "Making The Bright Choice". Sub title 'Ways to shape the bright days YOU seek' . Author Danica Forworth. The book is about deliberately changing things now, so you feel happy now and this then flows out an effects everything else in your life. It combines NLP, yoga philosophy and modern psychology in a down to earth, easy to read manner. I would like the cover to be happy, colourful, beautiful, artistic and hip. Maybe something hand drawn or painted. Something a woman would want to display and something that makes you smile and feel happy.
I don't want it to look like a romance novel and would prefer no photos of people. Pics are of other peoples covers I like. Thank you in advance. danica

Target Market(s)

woman 18-50

Industry/Entity Type

Business

Requirements
Must have
• happy feeling. professional look
Nice to have
• original drawing or painting
Should not have
• photos of real people, yellow smiley faces, sunsets, butterflies, yoga, tree, elements of my business logo

```html
<!DOCTYPE html>
<html lang="en">
<head>
<meta charset="utf-8">
<title>Making The Bright Choice – Book Cover</title>
<link href="https://fonts.googleapis.com/css2?family=Montserrat:wght@600;700&family=Oswald:wght@400&display=swap" rel="stylesheet">
<style>
  :root {
    --pink-light: #ff7aa8;
    --pink-mid: #fc5e95;
    --pink-deep: #e8306f;
    --ink: #2b1620;
    --white: #ffffff;
    --band-soft: rgba(255, 175, 205, 0.28);
    --band-deep: rgba(220, 20, 95, 0.30);
  }
  html, body {
    margin: 0;
    padding: 0;
    width: 910px;
    height: 1200px;
    overflow: hidden;
    background: #ffffff;
  }
  .cover {
    position: relative;
    width: 910px;
    height: 1200px;
    overflow: hidden;
    background: linear-gradient(165deg, var(--pink-light) 0%, var(--pink-mid) 50%, var(--pink-deep) 100%);
  }
  .cover__backdrop {
    position: absolute;
    inset: 0;
    background:
      radial-gradient(ellipse 380px 560px at 85% 88%, rgba(225, 25, 100, 0.55), transparent 70%),
      radial-gradient(ellipse 260px 480px at 6% 45%, rgba(255, 165, 200, 0.45), transparent 70%),
      radial-gradient(ellipse 520px 240px at 25% 80%, rgba(255, 150, 190, 0.35), transparent 70%);
  }
  .cover__bands {
    position: absolute;
    inset: 0;
    width: 910px;
    height: 1200px;
  }
  .band--soft { fill: var(--band-soft); }
  .band--deep { fill: var(--band-deep); }
  .band-line { fill: none; stroke: rgba(255, 190, 215, 0.45); stroke-width: 3; }
  .title {
    position: absolute;
    left: 0;
    right: 0;
    top: 0;
    margin: 0;
    text-align: center;
    font-family: "Montserrat", sans-serif;
    font-weight: 700;
    color: var(--white);
    line-height: 1;
  }
  .title__line {
    position: absolute;
    left: 0;
    right: 0;
    font-size: 120px;
    letter-spacing: 6px;
  }
  .title__line--first  { top: 100px; }
  .title__line--second { top: 232px; padding-left: 40px; }
  .title__line--third  { top: 364px; }
  .title__article {
    position: absolute;
    left: 160px;
    top: 252px;
    font-family: "Montserrat", sans-serif;
    font-weight: 600;
    font-size: 22px;
    letter-spacing: 3px;
    color: var(--white);
    transform-origin: left top;
    transform: rotate(-90deg) translateX(-86px);
  }
  .subtitle {
    position: absolute;
    top: 548px;
    left: 0;
    right: 0;
    margin: 0;
    text-align: center;
    font-family: "Oswald", sans-serif;
    font-weight: 400;
    font-size: 28px;
    letter-spacing: 0.5px;
    color: var(--ink);
  }
  .subtitle__accent { color: var(--white); }
  .cover__figure {
    position: absolute;
    left: 290px;
    top: 640px;
    width: 330px;
    height: 410px;
    background: radial-gradient(ellipse 50% 50% at 50% 48%, rgba(255, 255, 255, 0.42), rgba(255, 255, 255, 0.14) 55%, transparent 80%);
  }
  .author {
    position: absolute;
    top: 1120px;
    left: 0;
    right: 0;
    margin: 0;
    text-align: center;
    font-family: "Montserrat", sans-serif;
    font-weight: 700;
    font-size: 33px;
    letter-spacing: 2.5px;
    color: var(--white);
  }
</style>
</head>
<body>
  <main class="cover">
    <div class="cover__backdrop" role="img" aria-label="Soft layered pink petal and leaf shapes flowing across the background"></div>

    <svg class="cover__bands" viewBox="0 0 910 1200" aria-hidden="true">
      <path class="band--soft" d="M0 660 C220 600 520 700 910 900 L910 1000 C560 800 260 720 0 760 Z"/>
      <path class="band--deep" d="M910 380 C760 560 700 800 760 1200 L910 1200 Z"/>
      <path class="band--deep" d="M560 1200 C600 980 700 820 910 700 L910 1200 Z"/>
      <path class="band--soft" d="M0 120 C80 260 90 420 20 560 L0 560 Z"/>
      <path class="band--soft" d="M640 60 C760 160 820 300 800 470 C740 320 690 200 640 60 Z"/>
      <path class="band--soft" d="M0 1020 C180 960 360 1000 520 1200 L0 1200 Z"/>
      <path class="band-line" d="M0 720 C240 640 560 760 910 960"/>
      <path class="band-line" d="M0 930 C200 880 420 900 620 960"/>
    </svg>

    <h1 class="title">
      <span class="title__line title__line--first">MAKING</span>
      <span class="title__article">THE</span>
      <span class="title__line title__line--second">BRIGHT</span>
      <span class="title__line title__line--third">CHOICE</span>
    </h1>

    <p class="subtitle">WAYS TO SHAPE THE BRIGHT DAYS <span class="subtitle__accent">YOU</span> SEEK</p>

    <div class="cover__figure" role="img" aria-label="White illustration of a joyful figure with open arms encircled by leaves"></div>

    <p class="author">DANICA FORWORTH</p>
  </main>
</body>
</html>
```